Vitamin and Nutrition Ecommerce Site Needs a High End Website Design

We need a new and improved Homepage design for a leading Vitamin eCommerce business.
We supply our customers worldwide with leading brands of vitamin supplements and nutritional products at discounted prices.
The site design and layout must improve sales conversion and maximize the user experience staying on the site!

We will need to see;
A New Nutri Harbour stylized font (no logo)
High-End Modern Design
Easy Sales Conversion Experience
Excellent Layout, Fast Navigation
Quality Font style, Stylish Colour Palette Selection
Appropriate Spacing
Call To Action to Improve Sales Conversion
Web page should Look Clean and Minimalist

The design should improve sales, communicate easy to find products, facilitate fast ordering, have a modern and professional appearance centered toward a predominately female consumer.

Thank you for your interest in this project!

Current design can be found on this link;
www.nutriharbour.com.au/nutri/

Target Market(s)

80% Female 30-65 years

Industry/Entity Type

Business

Number of Pages Required

1 page

Colors

Designer to choose colors to be used in the design.

Requirements
Must have
• design must result improve sales conversion
• new Nutri Harbour font design
• search field
• attractive clean modern design
• stylish font and colour palette selection
Nice to have
• white background
Should not have
• cluttered or busy layout
• confusing navigation

```html
<!DOCTYPE html>
<html lang="en">
<head>
<meta charset="utf-8">
<title>Nutri Harbour – Home</title>
<link href="https://fonts.googleapis.com/css2?family=Montserrat:wght@400;500;600;700&family=Open+Sans:wght@400;600&display=swap" rel="stylesheet">
<style>
:root{
  --gold:#c9b07f;
  --gold-deep:#b89a5f;
  --band:#b1aa9b;
  --ink:#222222;
  --brown:#4b3b31;
  --body:#8a8a8a;
  --muted:#b5b5b5;
  --line:#e6e6e6;
  --panel:#f1f1f1;
  --foot:#f4f4f4;
  --ghost:#f1f1f1;
  --partner:#444444;
  --white:#ffffff;
}
*{box-sizing:border-box;margin:0;padding:0}
html,body{width:1200px;height:2875px;overflow:hidden;background:var(--white)}
body{position:relative;font-family:'Open Sans',Arial,sans-serif;color:var(--ink)}
.abs{position:absolute}

/* header */
.brand{left:250px;top:16px;font-family:'Montserrat',Arial,sans-serif;font-weight:500;font-size:29px;color:var(--brown);letter-spacing:-.3px}
.top-links{right:292px;top:30px;display:flex;gap:10px;font-size:8.5px;color:#9a9a9a;white-space:nowrap}
.top-icons{left:918px;top:27px;display:flex;gap:12px}
.nav-band{left:0;top:70px;width:1200px;height:30px;background:var(--band)}
.nav{left:248px;top:78px;display:flex;gap:12px;font-family:'Montserrat',Arial,sans-serif;font-size:9px;font-weight:600;color:var(--white);letter-spacing:.2px}

/* hero */
.hero-shadow{left:0;top:100px;width:1200px;height:272px;box-shadow:0 6px 14px rgba(0,0,0,.06)}
.ph{background:linear-gradient(160deg,#5a3e2c 0%,#3a2619 60%,#c48a2a 100%);border-radius:6px}
.hero-img{left:305px;top:125px;width:250px;height:230px}
.hero-hello{left:626px;top:142px;font-family:'Montserrat',Arial,sans-serif;font-size:21px;font-weight:500;color:var(--brown)}
.hero-title{left:626px;top:163px;font-family:'Montserrat',Arial,sans-serif;font-size:36px;font-weight:600;color:var(--brown)}
.hero-copy{left:626px;top:212px;width:290px;font-size:11.5px;line-height:15px;color:var(--body)}
.btn{background:var(--gold);color:var(--white);font-family:'Montserrat',Arial,sans-serif;font-weight:600;text-align:center;text-transform:uppercase}
.hero-btn{left:626px;top:294px;width:126px;height:30px;line-height:30px;font-size:11px}

/* features */
.features{left:230px;top:395px;width:740px;height:110px;display:flex}
.feature{flex:1;text-align:center;border-right:1px solid var(--line);padding-top:14px}
.feature:last-child{border-right:0}
.feature svg{display:block;margin:0 auto 10px}
.feature b{display:block;font-family:'Montserrat',Arial,sans-serif;font-size:10px;font-weight:600;letter-spacing:.3px}
.feature small{display:block;margin-top:4px;font-size:6.5px;color:var(--muted);letter-spacing:.5px}

/* section headings */
.sec-title{width:1200px;left:0;text-align:center;font-family:'Montserrat',Arial,sans-serif;font-weight:500;font-size:34px;letter-spacing:.5px}
.rule{height:3px;background:var(--gold)}
.sec-copy{left:360px;width:480px;text-align:center;font-size:10.5px;line-height:15px;color:var(--body)}

/* product cards */
.card{background:var(--white);box-shadow:0 8px 22px rgba(0,0,0,.12)}
.card-img{position:absolute;border-radius:4px}
.stars{position:absolute;width:100%;text-align:center;color:#e4a72a;font-size:11px;letter-spacing:1px}
.card-name{position:absolute;width:100%;text-align:center;font-family:'Montserrat',Arial,sans-serif;font-weight:700;font-size:11px;line-height:14px}
.card .btn{position:absolute;font-size:9px;height:22px;line-height:22px;border-radius:2px}
.ph-dark{background:linear-gradient(180deg,#2b2b2b,#111)}
.ph-jar{background:linear-gradient(180deg,#1e1e1e 0%,#1e1e1e 30%,#5bbf4a 31%,#5bbf4a 75%,#1e1e1e 76%)}
.ph-cream{background:linear-gradient(120deg,#f1eee4,#cfc7b3 60%,#4a7a3a)}
.ph-white{background:linear-gradient(180deg,#f7f7f7,#e5e9ee 60%,#c7ced6)}

/* feature stories */
.ghost-num{font-family:'Montserrat',Arial,sans-serif;font-weight:700;font-size:230px;color:var(--ghost);line-height:1}
.story-title{font-family:'Montserrat',Arial,sans-serif;font-weight:500;font-size:29px;line-height:30px;letter-spacing:.5px}
.story-copy{width:285px;font-size:11px;line-height:16px;color:var(--body)}
.ph-mix{background:linear-gradient(120deg,#1d1d1d 0%,#2e5a2a 45%,#e9e4ef 75%,#c8a9d9 100%);border-radius:8px}

/* new arrivals */
.price{position:absolute;width:100%;text-align:center;font-family:'Montserrat',Arial,sans-serif;font-size:15px;color:#666}
.price s{font-size:10px;color:#aaa;margin-right:6px}

/* offers */
.quote-card{left:270px;top:2135px;width:330px;height:395px;background:var(--white);box-shadow:0 8px 24px rgba(0,0,0,.13)}
.offer-panel{left:600px;top:2135px;width:330px;height:395px;background:var(--panel)}
.quote-title{left:308px;top:2193px;font-family:'Montserrat',Arial,sans-serif;font-weight:700;font-size:26px;line-height:29px}
.quote-copy{left:305px;top:2300px;width:250px;font-size:11px;line-height:16px;color:var(--body)}
.quote-by{left:445px;top:2416px;font-size:11px;color:var(--gold-deep);font-style:italic}
.dots{left:414px;top:2487px;display:flex;gap:5px}
.dots i{width:5px;height:5px;border-radius:50%;background:#cfcfcf}
.dots i:last-child{background:#777}
.offer-small{left:637px;top:2175px;font-family:'Montserrat',Arial,sans-serif;font-weight:700;font-size:20px}
.offer-big{left:637px;top:2200px;font-family:'Montserrat',Arial,sans-serif;font-weight:700;font-size:29px;color:var(--gold)}
.offer-next{left:637px;top:2236px;font-family:'Montserrat',Arial,sans-serif;font-weight:700;font-size:20px}
.offer-input{left:640px;top:2276px;width:210px;height:32px;background:var(--white);border:1px solid #e2e2e2}
.offer-btn{left:640px;top:2326px;width:126px;height:30px;line-height:30px;font-size:11px}
.offer-img{left:770px;top:2335px;width:150px;height:225px;background:linear-gradient(160deg,#222 0%,#111 55%,#c8622a 80%,#e2a24a 100%);border-radius:4px}

/* partners */
.partners{left:300px;top:2608px;width:600px;display:flex;justify-content:space-between;align-items:center;font-family:'Montserrat',Arial,sans-serif;font-size:20px;font-weight:500;color:var(--partner);letter-spacing:.5px}

/* footer */
.footer{left:0;top:2680px;width:1200px;height:195px;background:var(--foot)}
.foot-brand{left:250px;top:2727px;font-family:'Montserrat',Arial,sans-serif;font-weight:500;font-size:23px;color:var(--brown)}
.foot-col h4{font-family:'Montserrat',Arial,sans-serif;font-size:10px;font-weight:700;letter-spacing:.4px;margin-bottom:10px}
.foot-col p{font-size:9px;line-height:14px;color:#777}
.badges{display:flex;gap:10px}
.badges span{display:block;width:36px;height:22px;border-radius:3px}
.copyright{left:0;top:2845px;width:1200px;text-align:center;font-size:7.5px;color:#999}
</style>
</head>
<body>

<!-- header -->
<div class="abs brand">Nutri Harbour</div>
<div class="abs top-links"><span>MY ACCOUNT</span><span>MY WISHLIST</span><span>MY CART</span><span>CHECKOUT</span><span>REGISTER</span><span>LOG IN</span></div>
<div class="abs top-icons">
  <svg width="13" height="13" viewBox="0 0 13 13" fill="none" stroke="#222" stroke-width="2"><circle cx="5.5" cy="5.5" r="4"/><path d="M8.5 8.5l3.5 3.5"/></svg>
  <svg width="16" height="13" viewBox="0 0 16 13" fill="none" stroke="#222" stroke-width="1.6"><path d="M1 1h2.5l2 8h8l1.5-6H4.5"/><circle cx="6.5" cy="11.5" r="1"/><circle cx="12.5" cy="11.5" r="1"/></svg>
</div>
<div class="abs nav-band"></div>
<nav class="abs nav"><span>HOME</span><span>BRAND</span><span>SUPPLEMENTS</span><span>SPORTS NUTRITION</span><span>HAIRCARE</span><span>CHIROPRACTIC PILLOWS</span><span>HEALTH CONDITION</span><span>BEAUTY &amp; SKINCARE</span><span>GLUTEN FREE</span><span>ON SALE</span></nav>

<!-- hero -->
<div class="abs hero-shadow"></div>
<div class="abs ph hero-img" role="img" aria-label="Three brown jars of vitamin B capsules"></div>
<div class="abs hero-hello">Welcome to</div>
<div class="abs hero-title">Nutri Harbour</div>
<p class="abs hero-copy">Lorem ipsum dolor sit amet, consectetur adipiscing elit, sed do eiusmod tempor incididunt ut labore et dolore magna aliqua. Ut enim ad minim veniam, quis nostrud exercitation ullamco laboris nisi ut aliquip ex ea commodo consequat.</p>
<div class="abs btn hero-btn">Shop Now</div>

<!-- features -->
<div class="abs features">
  <div class="feature">
    <svg width="90" height="48" viewBox="0 0 90 48" fill="none" stroke="#c9b07f" stroke-width="2"><rect x="12" y="6" width="42" height="26" fill="#c9b07f"/><text x="33" y="24" text-anchor="middle" font-family="Montserrat,Arial,sans-serif" font-size="11" font-weight="700" fill="#fff" stroke="none">FREE</text><path d="M54 14h14l8 10v10H54z"/><path d="M12 34h64"/><circle cx="26" cy="40" r="5" fill="#fff"/><circle cx="64" cy="40" r="5" fill="#fff"/></svg>
    <b>FREE SHIPPING</b><small>ON ALL ORDERS OVER $90</small>
  </div>
  <div class="feature">
    <svg width="48" height="48" viewBox="0 0 48 48" fill="none" stroke="#c9b07f" stroke-width="2"><rect x="14" y="4" width="20" height="40"/><rect x="4" y="20" width="10" height="24"/><rect x="34" y="16" width="10" height="28"/><path d="M19 10h4M25 10h4M19 17h4M25 17h4M19 24h4M25 24h4M20 44v-9h8v9"/></svg>
    <b>OFFICIAL STOCKIST</b><small>OF MORE THAN 100 BRANDS</small>
  </div>
  <div class="feature">
    <svg width="48" height="48" viewBox="0 0 48 48" fill="none" stroke="#c9b07f" stroke-width="2"><rect x="16" y="4" width="16" height="7"/><path d="M14 11h20v33H14z"/><path d="M14 20h20M14 34h20"/><rect x="19" y="23" width="10" height="8" fill="#c9b07f"/></svg>
    <b>2 FREE SAMPLES</b><small>ON ALL ORDERS OVER $90</small>
  </div>
  <div class="feature">
    <svg width="48" height="48" viewBox="0 0 48 48" fill="none" stroke="#c9b07f" stroke-width="2"><path d="M3 12h6l5 20h22l5-14H12"/><circle cx="17" cy="39" r="3"/><circle cx="33" cy="39" r="3"/><path d="M30 2l9 3v7c0 5-4 8-9 10-5-2-9-5-9-10V5z" fill="#fff"/><path d="M26 11l3 3 5-6"/></svg>
    <b>VERIFIED TRUSTED STORE</b><small>RATING OF 4.9/5</small>
  </div>
</div>

<!-- our products -->
<h2 class="abs sec-title" style="top:598px">OUR PRODUCTS</h2>
<div class="abs rule" style="left:567px;top:650px;width:66px"></div>
<p class="abs sec-copy" style="top:675px">Lorem ipsum dolor sit amet, consectetur adipiscing elit, sed do eiusmod tempor incididunt ut labore et dolore magna aliqua. Ut enim ad minim veniam, quis</p>

<div class="abs card" style="left:210px;top:745px;width:240px;height:270px">
  <div class="card-img ph-dark" style="left:84px;top:30px;width:72px;height:150px" role="img" aria-label="Black bottle and box of men's moisturiser"></div>
  <div class="stars" style="top:188px">★★★★</div>
  <div class="card-name" style="top:206px">SOOTHING MENS<br>MOISTURISER</div>
  <div class="btn" style="left:75px;top:240px;width:90px">Read More</div>
</div>
<div class="abs card" style="left:480px;top:745px;width:240px;height:270px">
  <div class="card-img ph-jar" style="left:62px;top:40px;width:116px;height:140px" role="img" aria-label="Black jar with green label"></div>
  <div class="stars" style="top:188px">★★★★</div>
  <div class="card-name" style="top:206px">COMPLETE RESTWELL<br>DELUXE CONVENTIONAL FOAM</div>
  <div class="btn" style="left:75px;top:240px;width:90px">Read More</div>
</div>
<div class="abs card" style="left:755px;top:745px;width:240px;height:270px">
  <div class="card-img ph-cream" style="left:68px;top:40px;width:104px;height:140px" role="img" aria-label="Gel mask tube and box"></div>
  <div class="stars" style="top:188px">★★★★</div>
  <div class="card-name" style="top:206px">HYDRATING<br>GEL MASK</div>
  <div class="btn" style="left:75px;top:240px;width:90px">Read More</div>
</div>

<!-- exclusive offers -->
<div class="abs ghost-num" style="left:200px;top:1072px">01</div>
<h3 class="abs story-title" style="left:343px;top:1124px">EXCLUSIVE<br>OFFERS</h3>
<div class="abs rule" style="left:343px;top:1196px;width:70px"></div>
<p class="abs story-copy" style="left:343px;top:1218px">With savings of up to 70% off Recommended Retail Prices we invite you to choose to shop with us at Nutri Harbour! Inside our online store you will find we are a leading Australian health retailer specialising in Professional, Fast and Reliable service for all your natural healthcare needs.</p>
<div class="abs ph" style="left:670px;top:1092px;width:310px;height:265px" role="img" aria-label="Three jars of vitamin B capsules"></div>

<!-- skincare -->
<div class="abs ghost-num" style="left:720px;top:1398px">02</div>
<div class="abs ph-mix" style="left:200px;top:1400px;width:320px;height:265px" role="img" aria-label="Group of skincare and haircare products"></div>
<h3 class="abs story-title" style="left:587px;top:1436px">SKINCARE &amp;<br>HAIRCARE</h3>
<div class="abs rule" style="left:587px;top:1508px;width:70px"></div>
<p class="abs story-copy" style="left:587px;top:1530px">With savings of up to 70% off Recommended Retail Prices we invite you to choose to shop with us at Nutri Harbour! Inside our online store you will find we are a leading Australian health retailer specialising in Professional, Fast and Reliable service for all your natural healthcare needs.</p>

<!-- new arrivals -->
<h2 class="abs sec-title" style="top:1720px">NEW ARRIVALS</h2>
<div class="abs rule" style="left:567px;top:1772px;width:66px"></div>

<div class="abs card" style="left:210px;top:1822px;width:178px;height:248px">
  <div class="card-img ph-white" style="left:58px;top:28px;width:62px;height:100px" role="img" aria-label="White supplement bottle"></div>
  <div class="stars" style="top:152px">★★★★</div>
  <div class="card-name" style="top:168px;font-size:9.5px;line-height:12px">CALMREST PILLOW<br>SMALL SIZE SOFT DENSITY</div>
  <div class="price" style="top:199px"><s>$52.95</s>$28.00</div>
  <div class="btn" style="left:52px;top:225px;width:74px;height:18px;line-height:18px;font-size:8px">Add to Cart</div>
</div>
<div class="abs card" style="left:413px;top:1822px;width:178px;height:248px">
  <div class="card-img ph-white" style="left:62px;top:28px;width:54px;height:100px" role="img" aria-label="White supplement bottle with capsules"></div>
  <div class="stars" style="top:152px">★★★★</div>
  <div class="card-name" style="top:168px;font-size:9.5px;line-height:12px">CALMREST PILLOW STANDARD<br>SIZE SUPER SOFT DENSITY</div>
  <div class="price" style="top:199px"><s>$60.00</s>$25.00</div>
  <div class="btn" style="left:52px;top:225px;width:74px;height:18px;line-height:18px;font-size:8px">Add to Cart</div>
</div>
<div class="abs card" style="left:617px;top:1822px;width:178px;height:248px">
  <div class="card-img ph-white" style="left:58px;top:28px;width:62px;height:100px" role="img" aria-label="White supplement bottle"></div>
  <div class="stars" style="top:152px">★★★★</div>
  <div class="card-name" style="top:168px;font-size:9.5px;line-height:12px">CALMREST PILLOW<br>SMALL SIZE SOFT DENSITY</div>
  <div class="price" style="top:199px"><s>$52.95</s>$28.00</div>
  <div class="btn" style="left:52px;top:225px;width:74px;height:18px;line-height:18px;font-size:8px">Add to Cart</div>
</div>
<div class="abs card" style="left:820px;top:1822px;width:178px;height:248px">
  <div class="card-img ph" style="left:42px;top:28px;width:94px;height:100px" role="img" aria-label="Three brown vitamin jars"></div>
  <div class="stars" style="top:152px">★★★★</div>
  <div class="card-name" style="top:168px;font-size:9.5px;line-height:12px">ACNE CONTROL TABLETS EXTRA<br>STRENGTH NEW</div>
  <div class="price" style="top:199px"><s>$100.00</s>$95.00</div>
  <div class="btn" style="left:52px;top:225px;width:74px;height:18px;line-height:18px;font-size:8px">Add to Cart</div>
</div>

<!-- testimonials and offer -->
<div class="abs offer-panel"></div>
<div class="abs quote-card"></div>
<h3 class="abs quote-title">WHAT PEOPLE<br>ARE SAYING</h3>
<p class="abs quote-copy">With savings of up to 70% off Recommended Retail Prices we invite you to choose to shop with us at Nutri Harbour! Inside our online store you will find we are a leading Australian health retailer specialising in Professional, Fast and Reliable service for all your natural healthcare needs.</p>
<div class="abs quote-by">- Name , Designation</div>
<div class="abs dots"><i></i><i></i><i></i><i></i></div>
<div class="abs offer-small">SPECIAL OFFERS</div>
<div class="abs offer-big">GET 10% OFF</div>
<div class="abs offer-next">YOUR NEXT ORDER</div>
<div class="abs offer-input"></div>
<div class="abs btn offer-btn">Signup</div>
<div class="abs offer-img" role="img" aria-label="Coffee bag and small product box"></div>

<!-- partners -->
<svg class="abs" style="left:250px;top:2620px" width="12" height="22" viewBox="0 0 12 22" fill="none" stroke="#999" stroke-width="1.5"><path d="M10 2L2 11l8 9"/></svg>
<div class="abs partners">
  <span>Lumen</span>
  <span>Solenne</span>
  <span>Corvelle</span>
  <span>Aurelis</span>
</div>
<svg class="abs" style="left:938px;top:2620px" width="12" height="22" viewBox="0 0 12 22" fill="none" stroke="#999" stroke-width="1.5"><path d="M2 2l8 9-8 9"/></svg>

<!-- footer -->
<footer class="abs footer"></footer>
<div class="abs foot-brand">Nutri Harbour</div>
<div class="abs foot-col" style="left:425px;top:2705px"><h4>USEFUL LINKS</h4><p>About Us</p><p>Customer Service</p><p>Privacy Policy</p></div>
<div class="abs foot-col" style="left:612px;top:2705px"><h4>PRODUCTS</h4><p>About Us</p><p>Contact Us</p><p>Customer Service</p><p>Privacy Policy</p></div>
<div class="abs foot-col" style="left:775px;top:2705px"><h4>MOBILE APP</h4>
  <div class="badges"><span style="background:#e9a24a"></span><span style="background:#f2c230"></span><span style="background:#d9d9d9"></span></div>
</div>
<div class="abs copyright">© 2017 Nutri Harbour All Rights Reserved</div>

</body>
</html>
```